Lanternfield Billboard - Financial Services Company (Investments, Tax Planning and Insurance)

Our new office has a billboard directly above the office building. We'd like something eye-catching with a strong Call to Action, with the main part of the billboard being under 7 words if possible. We'd like you to include a way to get ahold of us (either our website lanternfieldllc.example or our phone number 302-418-2967. You may also include in small font something to indicate that we've been serving the area since 1980 (the DE area, the tri-state area, the Copperleaf Basin, etc.)

We offer financial planning, tax planning, and insurance, and we help our clients to focus on their goals and happiness by providing everything they need for lifelong wealth under one roof.

Our logos are attached, we use a triangle logo with green and gray. We use the tagline "experience lifelong wealth" but this does not need to be included.

Potential ideas we have seen from other financial companies-
- the concept that the driver spends more time looking at billboards than planning for their retirement
-something along the lines of "everything you need for your finances is in this building right here" planning, investments, taxes, insurance"
-don't spend your time worrying about retirement, let us help you plan for it
-are you working for your money, or is it working for you?
- retirement takes planning, we're here to help
- ready to retire? talk to us
- need investment advice?
- need help investing?
- crossing your fingers isn't a retirement plan. we can help.
- retiring soon? you need help.

Those are just general ideas, please feel free to be creative.

brand colors:
#00b585
#00b185
#000000
#ffffff
#6d6f75
#6d6f75
#6f7074
#021712
#052e24

```html
<!DOCTYPE html>
<html lang="en">
<head>
<meta charset="utf-8">
<title>Lanternfield Billboard</title>
<link rel="stylesheet" href="https://fonts.googleapis.com/css2?family=Jost:wght@400;500&display=swap">
<style>
  :root {
    --brand-green: #00b185;
    --bubble-white: #ffffff;
    --slate-gray: #6d6f75;
    --deep-ink: #021712;
    --shadow: rgba(2, 23, 18, 0.28);
  }
  html, body {
    margin: 0;
    padding: 0;
    overflow: hidden;
    background: var(--brand-green);
  }
  .billboard {
    position: relative;
    width: 1200px;
    height: 576px;
    background: var(--brand-green);
    overflow: hidden;
  }
  .billboard-art {
    position: absolute;
    inset: 0;
    width: 1200px;
    height: 576px;
  }
  .speech-bubble,
  .brand-bubble {
    fill: var(--bubble-white);
    filter: drop-shadow(2px 5px 6px var(--shadow));
  }
  .headline {
    font-family: "Jost", sans-serif;
    font-weight: 500;
    font-size: 82px;
    letter-spacing: 0.035em;
    fill: var(--slate-gray);
  }
  .offer {
    font-family: "Jost", sans-serif;
    font-weight: 500;
    font-size: 43px;
    letter-spacing: 0.01em;
    fill: var(--brand-green);
  }
  .phone {
    font-family: "Jost", sans-serif;
    font-weight: 500;
    font-size: 70px;
    fill: var(--slate-gray);
  }
  .since-line {
    font-family: "Jost", sans-serif;
    font-weight: 400;
    font-size: 42px;
    word-spacing: 0.22em;
    fill: var(--deep-ink);
  }
  .brand-name {
    font-family: "Jost", sans-serif;
    font-weight: 500;
    font-size: 19px;
    fill: var(--slate-gray);
  }
</style>
</head>
<body>
  <main class="billboard">
    <svg class="billboard-art" viewBox="0 0 1200 576" xmlns="http://www.w3.org/2000/svg">
      <path class="speech-bubble"
        d="M251,47.5 H949 A137 126 0 0 1 1086 173.5 V307 A137 126 0 0 1 949 433 H447
           C420,500 340,532 271,549 C305,510 305,470 295,433 H251
           A137 126 0 0 1 114 307 V173.5 A137 126 0 0 1 251 47.5 Z"/>

      <text class="headline" x="230" y="182">NEED INVESTMENT</text>
      <text class="headline" x="226" y="266">ADVICE?</text>
      <text class="offer" x="224" y="325">FREE CONSULTATION</text>
      <text class="phone" x="222" y="386">302-418-2967</text>

      <text class="since-line" x="449" y="518">serving the area since 1980</text>

      <path class="brand-bubble"
        d="M68,416 H160 A18 18 0 0 1 178 434 V487 A18 18 0 0 1 160 505 H95
           C90,510 90,518 98,526 C85,521 72,516 65,504
           A18 18 0 0 1 50 487 V434 A18 18 0 0 1 68 416 Z"/>
      <text class="brand-name" x="114" y="467" text-anchor="middle">Lanternfield</text>
    </svg>
  </main>
</body>
</html>
```